TBrenwick Business Cards & Letterhead

I have a logo but need a design for some new business cards. We are a Design-Build Firm that specializes in the design and construction of commercial projects.
the cards need to be professional. no cartoon stuff.
i would like to have the cards in AI format so I can update the card as needed. Logo is provided.
Our Address is: 4718 Fenmoor Ct. Elmridge, Vermont 05412

```html
<!DOCTYPE html>
<html lang="en">
<head>
<meta charset="utf-8">
<title>TBrenwick Business Card</title>
<link rel="stylesheet" href="https://fonts.googleapis.com/css2?family=Questrial&display=swap">
<style>
  :root {
    --backdrop: #616163;
    --card: #ffffff;
    --brand-blue: #0068a5;
    --ink: #111111;
    --wordmark: #333333;
  }
  * { margin: 0; padding: 0; box-sizing: border-box; }
  html, body { width: 1200px; height: 1050px; overflow: hidden; }
  body {
    background: var(--backdrop);
    font-family: "Questrial", sans-serif;
    position: relative;
  }
  .card {
    position: absolute;
    left: 342px;
    width: 516px;
    height: 302px;
    background: var(--card);
    border-radius: 18px;
    overflow: hidden;
  }
  .card--front { top: 183px; }
  .card--back { top: 553px; }

  .check {
    position: absolute;
    width: 16.5px;
    height: 16.5px;
    background: var(--brand-blue);
  }

  .wave-field {
    position: absolute;
    left: 0;
    width: 100%;
  }
  .card--front .wave-field {
    top: 156px;
    height: 146px;
    background: linear-gradient(180deg, rgba(255,255,255,0) 0%, rgba(242,196,196,0.25) 45%, rgba(175,190,210,0.35) 100%);
  }
  .card--back .wave-field {
    top: 68px;
    height: 148px;
    background: radial-gradient(ellipse at 30% 40%, rgba(230,166,196,0.28), rgba(255,255,255,0) 60%),
                radial-gradient(ellipse at 70% 55%, rgba(159,198,222,0.32), rgba(255,255,255,0) 60%);
  }

  .front-brand {
    position: absolute;
    left: 40px;
    top: 140px;
    display: flex;
    align-items: center;
    gap: 7px;
    color: var(--brand-blue);
    font-size: 22px;
  }
  .front-brand .mark-square {
    width: 12px;
    height: 12px;
    background: var(--brand-blue);
  }

  .divider {
    position: absolute;
    left: 215px;
    top: 56px;
    width: 2px;
    height: 189px;
    background: var(--brand-blue);
    border-radius: 1px;
  }

  .contact {
    position: absolute;
    right: 58px;
    top: 95px;
    text-align: right;
    color: var(--ink);
    line-height: 1;
  }
  .contact .person-name {
    font-size: 22px;
    letter-spacing: 1.6px;
  }
  .contact .person-title {
    font-size: 9px;
    letter-spacing: 1.8px;
    margin-top: 4px;
  }
  .contact .company {
    font-size: 13.5px;
    letter-spacing: 2.2px;
    margin-top: 23px;
  }
  .contact .line {
    font-size: 10.3px;
    letter-spacing: 2.1px;
    margin-top: 4.7px;
  }
  .contact .company + .line { margin-top: 3.5px; }

  .wordmark {
    position: absolute;
    left: 0;
    width: 100%;
    top: 126px;
    text-align: center;
    font-size: 56px;
    letter-spacing: 2px;
    color: var(--wordmark);
    line-height: 1;
  }
</style>
</head>
<body>

<section class="card card--front">
  <div class="wave-field" role="img" aria-label="Decorative fine curved line pattern in soft pink and blue"></div>

  <span class="check" style="left:0;top:13px"></span>
  <span class="check" style="left:16.4px;top:29.3px"></span>
  <span class="check" style="left:0;top:45.7px"></span>
  <span class="check" style="left:33.4px;top:45.7px"></span>

  <span class="check" style="left:466.5px;top:0"></span>
  <span class="check" style="left:500px;top:0"></span>
  <span class="check" style="left:450px;top:16px"></span>
  <span class="check" style="left:483.5px;top:16px"></span>
  <span class="check" style="left:466.5px;top:32px"></span>
  <span class="check" style="left:500px;top:32px"></span>

  <div class="front-brand"><span class="mark-square"></span><span>TBrenwick</span></div>

  <div class="divider"></div>

  <div class="contact">
    <p class="person-name">MARCUS ELLERY</p>
    <p class="person-title">FOUNDER/PRESIDENT</p>
    <p class="company">TBrenwick, Inc</p>
    <p class="line">4718 Fenmoor Ct.</p>
    <p class="line">Elmridge, Vermont 05412</p>
    <p class="line">Office 919-555-0148</p>
  </div>
</section>

<section class="card card--back">
  <div class="wave-field" role="img" aria-label="Decorative flowing wave lines in pink and blue"></div>

  <span class="check" style="left:466.5px;top:11px"></span>
  <span class="check" style="left:500px;top:11px"></span>
  <span class="check" style="left:483.5px;top:27.5px"></span>
  <span class="check" style="left:466.5px;top:44px"></span>

  <span class="check" style="left:0;top:235.5px"></span>
  <span class="check" style="left:33.4px;top:235.5px"></span>
  <span class="check" style="left:16.4px;top:252px"></span>
  <span class="check" style="left:0;top:268.4px"></span>

  <p class="wordmark">TBRENWICK</p>
</section>

</body>
</html>
```